Business Cards For A cell Phone Company
Linden Cellular
Business Cards For A cell Phone Company - Retailers
Creative Brief
Simple
Tobias Krell
Operations Manager
2864 Belmore Ave Cincinnati OH 45219
tobias.krell@lindencellular-mail.com
www.lindencellular-mail.com
Concepts
Business Cards/Letterhead/ Envelopes/Notepads/Tshirt/labels for quiet tin crate
Business cards and company letter head for Orchard Noodle Court

```html
<!DOCTYPE html>
<html lang="en">
<head>
<meta charset="utf-8">
<title>Linden Cellular – Business Cards</title>
<link href="https://fonts.googleapis.com/css2?family=Titillium+Web:wght@400;600;700&display=swap" rel="stylesheet">
<style>
  :root {
    --stage: #e9e7e4;
    --card: #ffffff;
    --red: #c8102e;
    --red-dark: #8e0a1f;
    --grey: #9a9a9a;
    --grey-light: #d4d4d4;
    --ink: #555555;
  }
  * { margin: 0; padding: 0; box-sizing: border-box; }
  html, body { width: 1200px; height: 828px; overflow: hidden; }
  body {
    background: var(--stage);
    font-family: "Titillium Web", Arial, sans-serif;
    position: relative;
  }
  .card {
    position: absolute;
    top: 260px;
    width: 540px;
    height: 309px;
    background: var(--card);
    box-shadow: 0 6px 18px rgba(0,0,0,0.18);
    overflow: hidden;
  }
  .card--front { left: 40px; }
  .card--back { left: 620px; }

  .brand {
    display: flex;
    align-items: center;
    gap: 12px;
    color: var(--red);
    font-weight: 700;
    text-transform: uppercase;
    letter-spacing: 1px;
    white-space: nowrap;
  }
  .brand__square {
    width: 38px; height: 38px;
    background: var(--red);
    flex: none;
  }
  .card--front .brand {
    position: absolute;
    left: 50%; top: 50%;
    transform: translate(-50%, -50%);
    font-size: 30px;
  }
  .card--back .brand {
    position: absolute;
    left: 30px; top: 150px;
    font-size: 19px;
    gap: 10px;
  }
  .card--back .brand__square { width: 26px; height: 26px; }

  .swoosh { position: absolute; inset: 0; width: 100%; height: 100%; }

  .contact {
    position: absolute;
    left: 280px; top: 22px;
    color: var(--ink);
    font-size: 11px;
    line-height: 1.4;
  }
  .contact__name {
    color: var(--red);
    font-weight: 700;
    font-size: 16px;
    text-transform: uppercase;
    letter-spacing: 0.5px;
  }
  .contact__title { font-size: 12px; margin-bottom: 8px; }
  .contact__address { margin-bottom: 8px; }
  .contact__line { display: flex; align-items: center; gap: 6px; }
  .contact__line svg { width: 11px; height: 11px; flex: none; }

  .website {
    position: absolute;
    right: 8px; bottom: 8px;
    writing-mode: vertical-rl;
    transform: rotate(180deg);
    color: #ffffff;
    font-size: 9px;
    letter-spacing: 0.5px;
    white-space: nowrap;
  }
</style>
</head>
<body>
  <section class="card card--front">
    <div class="brand"><span class="brand__square"></span>Linden Cellular</div>
  </section>

  <section class="card card--back">
    <svg class="swoosh" viewBox="0 0 540 309" preserveAspectRatio="none" aria-hidden="true">
      <defs>
        <linearGradient id="redBand" x1="0" y1="1" x2="1" y2="0">
          <stop offset="0" stop-color="var(--red-dark)"/>
          <stop offset="1" stop-color="var(--red)"/>
        </linearGradient>
      </defs>
      <path d="M0 300 C 200 292, 400 240, 540 120 L540 309 L0 309 Z" fill="var(--grey-light)"/>
      <path d="M60 309 C 260 292, 420 250, 540 150 L540 309 Z" fill="url(#redBand)"/>
      <path d="M0 285 C 200 280, 400 232, 540 105" fill="none" stroke="var(--grey)" stroke-width="3"/>
    </svg>

    <div class="brand"><span class="brand__square"></span>Linden Cellular</div>

    <div class="contact">
      <p class="contact__name">Tobias Krell</p>
      <p class="contact__title">Operations Manager</p>
      <p class="contact__address">2864 Belmore Ave<br>Cincinnati OH 45219</p>
      <p class="contact__line">
        <svg viewBox="0 0 12 12"><rect x="0.5" y="2" width="11" height="8" fill="none" stroke="var(--red)"/><path d="M0.5 2 L6 7 L11.5 2" fill="none" stroke="var(--red)"/></svg>
        tobias.krell@lindencellular-mail.com
      </p>
      <p class="contact__line">
        <svg viewBox="0 0 12 12"><path d="M2 1 L4.5 1 L5.5 4 L4 5 C5 7 6 8 8 9 L9 7.5 L11.5 8.5 L11.5 11 C6 11 1 6 1 1 Z" fill="var(--red)"/></svg>
        513 555 0142
      </p>
    </div>

    <p class="website">www.lindencellular-mail.com</p>
  </section>
</body>
</html>
```